Looking for an amazing business card for a thriving DJ business

We need a business card design for a DJ company based in South Florida. The DJ company specializes in weddings, parties, bar mitzvahs, corporate events, proms, and reunions. We are looking for a modern, simple business card design. The card should state DJ Marlow K.
Updates

The name on the card should be DJ Marlow K

Industry/Entity Type

Entertainment Industry

Contact Information for Business Card

DJ Marlow K
512.447.2086
atxdjmarlowk@quellmail.com
https://www.facebook.com/DjMarlowK/
https://www.instagram.com/djmarlow.k/
www.djmarlowk.net

Font styles to use
Serif
Sans Serif

Requirements
Must have
• My business card has to be awesome.
Should not have
• The card has to have personality.

```html
<!DOCTYPE html>
<html lang="en">
<head>
<meta charset="utf-8">
<title>DJ Marlow K — Business Card</title>
<link rel="stylesheet" href="https://fonts.googleapis.com/css2?family=Poppins:wght@400;500&display=swap">
<style>
  :root {
    --page-bg: #e9e4dc;
    --card-frost: #e6e2dc;
    --card-frost-edge: #d4cfc7;
    --panel-dark: #22332f;
    --panel-mid: #3b4a46;
    --gold: #a8781f;
    --gold-light: #c89a45;
    --ink-dark: #1f302c;
    --text-light: #f1ede6;
    --text-soft: #e3ddd2;
  }
  * { box-sizing: border-box; margin: 0; padding: 0; }
  html, body {
    width: 970px; height: 1200px; overflow: hidden;
    background: var(--page-bg);
    font-family: "Poppins", sans-serif;
  }
  .canvas { position: relative; width: 970px; height: 1200px; }
  .card {
    position: absolute; left: 185px; top: 75px;
    width: 600px; height: 1050px;
    border-radius: 28px; overflow: hidden;
    background: linear-gradient(160deg, #f1eee9 0%, var(--card-frost) 55%, var(--card-frost-edge) 100%);
    box-shadow: 0 12px 40px rgba(40, 34, 26, 0.18);
  }
  .card-art { position: absolute; inset: 0; }
  .brand-mark {
    position: absolute; left: 150px; top: 120px;
    width: 300px; height: 300px;
    display: flex; align-items: center; justify-content: center;
  }
  .brand-ring {
    position: absolute; inset: 0;
    border: 3px solid var(--ink-dark); border-radius: 50%;
  }
  .brand-name {
    font-weight: 500; font-size: 40px; color: var(--ink-dark);
    letter-spacing: 1px;
  }
  .dj-name {
    position: absolute; left: 0; right: 0; top: 618px;
    text-align: center; font-weight: 500; font-size: 38px;
    color: var(--text-light); letter-spacing: 1px;
  }
  .contact-icons {
    position: absolute; left: 0; right: 0; top: 703px;
    display: flex; justify-content: center; align-items: center; gap: 9px;
  }
  .rule { width: 74px; height: 2px; background: var(--gold); margin: 0 14px; }
  .icon-dot {
    width: 36px; height: 36px; border-radius: 50%;
    background: var(--gold-light);
    display: flex; align-items: center; justify-content: center;
  }
  .contact-list {
    position: absolute; left: 0; right: 0; top: 768px;
    list-style: none; text-align: center;
    font-size: 25px; line-height: 37.5px; color: var(--text-soft);
  }
  .site-band {
    position: absolute; left: 0; right: 0; bottom: 0; height: 75px;
    display: flex; align-items: center; justify-content: center;
    font-size: 25px; color: var(--text-soft);
  }
</style>
</head>
<body>
<div class="canvas">
  <div class="card">
    <svg class="card-art" width="600" height="1050" viewBox="0 0 600 1050" aria-hidden="true">
      <defs>
        <linearGradient id="panelShade" x1="0" y1="0" x2="0" y2="1">
          <stop offset="0" stop-color="#22332f"/>
          <stop offset="1" stop-color="#3b4a46"/>
        </linearGradient>
        <linearGradient id="goldShade" x1="0" y1="0" x2="1" y2="0">
          <stop offset="0" stop-color="#8e6418"/>
          <stop offset="0.5" stop-color="#b9872c"/>
          <stop offset="1" stop-color="#9c6d1c"/>
        </linearGradient>
      </defs>
      <path d="M0 545 C 140 470, 380 455, 600 525 L 600 560 C 400 500, 180 510, 0 600 Z" fill="url(#goldShade)"/>
      <path d="M0 600 C 180 520, 400 515, 600 560 L 600 965 L 0 965 Z" fill="url(#panelShade)"/>
      <path d="M110 575 C 260 520, 430 515, 600 545 L 600 550 C 430 525, 270 530, 110 575 Z" fill="#f3efe8"/>
      <rect x="0" y="965" width="600" height="10" fill="#e8e2d6"/>
      <rect x="0" y="975" width="600" height="75" fill="url(#goldShade)"/>
    </svg>

    <div class="brand-mark">
      <span class="brand-ring"></span>
      <span class="brand-name">Soundcrest</span>
    </div>

    <h1 class="dj-name">DJ Marlow K</h1>

    <div class="contact-icons">
      <span class="rule"></span>
      <span class="icon-dot" aria-label="phone">
        <svg width="16" height="22" viewBox="0 0 16 22"><rect x="2" y="1" width="12" height="20" rx="2" fill="none" stroke="#fff" stroke-width="2"/><rect x="6" y="16" width="4" height="2" fill="#fff"/></svg>
      </span>
      <span class="icon-dot" aria-label="email">
        <svg width="22" height="16" viewBox="0 0 22 16"><rect x="1" y="1" width="20" height="14" rx="1" fill="none" stroke="#fff" stroke-width="2"/><path d="M1 1 L11 9 L21 1" fill="none" stroke="#fff" stroke-width="2"/></svg>
      </span>
      <span class="icon-dot" aria-label="social page"></span>
      <span class="icon-dot" aria-label="photo profile"></span>
      <span class="rule"></span>
    </div>

    <ul class="contact-list">
      <li>512.447.2086</li>
      <li>atxdjmarlowk@quellmail.com</li>
      <li>www.friendwall.com/DjMarlowK/</li>
      <li>www.snapgrid.com/djmarlow.k/</li>
    </ul>

    <div class="site-band">www.djmarlowk.net</div>
  </div>
</div>
</body>
</html>
```